BELVORA needs a label for a Surface Cleaner with Alcohol

INTRODUCTION:
We are BELVORA, an experienced Spanish family-owned business specialized in manufacturing and distributing low-cost high-quality cleaning products in Spain, France and Portugal.

We are launching a new SURFACE CLEANER WITH ALCOHOL and we need an eye-catching label! We want to put your creativity to work! :D

CONCEPT:
Surface cleaner containing alcohol (not a disinfectant or hand sanitizer)

2 sizes

1) 750 ml PET cilinder white bottle with spray (bottle measures: 70mm diameter 230 mm height w/o spray)
Labels size (120mm base x 160mm height), 1 front label + 1 back label

2) 60 ml PET cilinder white bottle with spray (bottle 90mm height w/o spray x 35mm diameter) 1 label
Label size 110mm base x 60mm height

The design of the larger bottle must be adapted to the smaller bottle so as to make a collection

Label is in Spanish language (we are providing texts below)

GOAL:
To create a clean minimalist label with a “pharmaceutical” look and feel. Ideally by using colors and shapes to evoke a pharma green cross without explicitly using it. The pharma look and feel has to be visible from some distance. It must inspire safety and protection.

If you do mockups please use a 3D image of a bottle with sprayer (not the photo attached because it will look bad)

We love to see your ideas and be surprised with your proposals!

Thank you!

Target Market(s)

General public (non-professional) target, drugstore/supermaket, Spanish market mainly at the moment

Industry/Entity Type

Cleaning Product

Requirements
Must have
• Label front must have:
• - words: "LIMPIADOR HIGIENIZANTE" and "con ALCOHOL"
• - colors: white, pharma-looking light green, and a touch of blue
• - logo: BELVORA (brand), with the same pharma-looking green color
• - for the small bottle: a plane icon to point out that is suitable for travelling
• Label back side must contain this:
• - marketing text:
• “Limpiador higienizante para todo tipo de superfícies lavables. Su gran poder limpiador e higienizante elimina eficazmente la suciedad de zonas de contacto tales como asientos, inodoros, duchas, vidrios, pomos, manetas, asideros, barandillas, mesas, encimeras, suelos, mostradores, vitrinas, etc. No contiene lejía.”
• - icons:
• A column of 4-5 minimalist icons to clearly point out the applications (door knobs, seats, sink, handrail, toilet, floor, shower, glass,…) see icon examples attached for styling inspiration
• - legal text:
• “Líquido y vapores muy inflamables. Provoca irritación ocular grave. Puede provocar somnolencia o vértigo. Mantener alejado del calor, de superficies calientes, de chispas, de llamas abiertas y de cualquier otra fuente de ignición. No fumar. Mantener el recipiente herméticamente cerrado. Evitar respirar el polvo/el humo/el gas/la niebla/los vapores/el aerosol. Llevar guantes/prendas/gafas/máscara de protección. En caso de incendio emplear niebla de agua, espuma, productos químicos secos o dióxido de carbono ( CO2 ) para apagarlo. Almacenar en un lugar bien ventilado. Mantener el recipiente cerrado herméticamente. Mantener en lugar fresco.”
• - company identification:
• TOLMEN CASTRA SL
• B47392618
• C/ Valdemur 317 2-4
• 08051 Barcelona
• - pictograms: see the pictograms file
Nice to have
• Would be great to include:
• - seal: round seal with one or two words inside to give the feeling of “certified” or “approved”
• - a percetage number, like "100 % efectivo”
• - a small red “plus” sign referring for example to “+ higiene”
Should not have
• A plain green or red cross alone

```html
<!DOCTYPE html>
<html lang="es">
<head>
<meta charset="utf-8">
<title>BELVORA · Limpiador Higienizante con Alcohol</title>
<link rel="stylesheet" href="https://fonts.googleapis.com/css2?family=Saira+Semi+Condensed:wght@600&family=Maven+Pro:wght@500;600;700&display=swap">
<style>
  :root {
    --canvas-bg: #eeeeee;
    --label-white: #ffffff;
    --pharma-green: #22a03c;
    --pharma-green-dark: #1c8f33;
    --pharma-green-light: #52cc5e;
    --emblem-tone-a: #3fb34f;
    --emblem-tone-b: #7ad585;
    --accent-blue: #3f86dc;
    --accent-blue-light: #86c0f7;
    --alcohol-blue: #6fb0f2;
  }
  html, body {
    margin: 0;
    padding: 0;
    width: 1067px;
    height: 1200px;
    overflow: hidden;
    background: var(--canvas-bg);
  }
  .label-canvas {
    display: block;
    width: 1067px;
    height: 1200px;
  }
  .label-sheet { fill: var(--label-white); }
  .product-title {
    font-family: "Saira Semi Condensed", "Arial Narrow", sans-serif;
    font-weight: 600;
    fill: var(--pharma-green);
  }
  .claim-small {
    font-family: "Maven Pro", Arial, sans-serif;
    font-weight: 600;
    fill: var(--pharma-green);
  }
  .claim-alcohol {
    font-family: "Maven Pro", Arial, sans-serif;
    font-weight: 500;
    fill: var(--alcohol-blue);
  }
  .brand-band { fill: var(--pharma-green); }
  .brand-tab { fill: var(--pharma-green-light); }
  .brand-name {
    font-family: "Maven Pro", Arial, sans-serif;
    font-weight: 700;
    fill: var(--label-white);
  }
</style>
</head>
<body>
<svg class="label-canvas" viewBox="0 0 1067 1200" xmlns="http://www.w3.org/2000/svg">
  <defs>
    <linearGradient id="top-stripe" x1="0" y1="0" x2="1" y2="0">
      <stop offset="0" stop-color="var(--accent-blue)"/>
      <stop offset="0.5" stop-color="var(--accent-blue-light)"/>
      <stop offset="1" stop-color="var(--accent-blue)"/>
    </linearGradient>
    <linearGradient id="emblem-fill" x1="0" y1="0" x2="1" y2="1">
      <stop offset="0" stop-color="var(--emblem-tone-a)"/>
      <stop offset="1" stop-color="var(--emblem-tone-b)"/>
    </linearGradient>
  </defs>

  <!-- Front label -->
  <rect class="label-sheet" x="263" y="120" width="540" height="960"/>

  <!-- Top blue stripe -->
  <rect x="263" y="134" width="540" height="18" fill="url(#top-stripe)"/>

  <!-- Product name -->
  <text class="product-title" x="533" y="282" text-anchor="middle" font-size="80" textLength="398" lengthAdjust="spacingAndGlyphs">LIMPIADOR</text>
  <text class="product-title" x="533" y="342" text-anchor="middle" font-size="80" textLength="477" lengthAdjust="spacingAndGlyphs">HIGIENIZANTE</text>

  <!-- Emblem area -->
  <rect class="emblem-area" role="img" aria-label="Emblema verde de flechas en molinete alrededor de una cruz blanca" x="378" y="415" width="310" height="310" rx="6" fill="url(#emblem-fill)"/>

  <!-- Alcohol claim -->
  <text class="claim-small" x="533" y="830" text-anchor="middle" font-size="30">con</text>
  <text class="claim-alcohol" x="533" y="891" text-anchor="middle" font-size="66" textLength="293" lengthAdjust="spacingAndGlyphs">ALCOHOL</text>
  <text class="claim-small" x="533" y="926" text-anchor="middle" font-size="30">isopropílico</text>

  <!-- Brand band -->
  <rect class="brand-band" x="263" y="1057" width="540" height="22"/>
  <path class="brand-tab" d="M360 1079 V996 Q360 978 378 978 H713 Q731 978 731 996 V1079 Z"/>
  <text class="brand-name" x="545" y="1050" text-anchor="middle" font-size="52" textLength="260" lengthAdjust="spacingAndGlyphs">BELVORA</text>
</svg>
</body>
</html>
```